indépendant en tant que Massothérapeute et Préparateur Mental, j'ai besoin de ...

Massothérapeute et préparateur mental indépendant, je recherche une carte de visite sobre et dynamique, sans images liées au massage ou à la préparation mentale mais intégrant mon logo. Les couleurs que j'aime bien sont : Blanc, gris, anthracite, noir et jaune

Contact Information for Business Card

carte de préférence Horizontale
neutre qui puisse toucher le deux domaines Massothérapie et préparation mentale

Requirements
Must have
• mon projet doit intégrer au recto:
LOGO
Loïc Vermande
078 315 26 49
info@loicvermande-exemple.ch
et éventuellement www.loicvermande-exemple.ch

et au verso les deux adresses:

Chemin des Ormelets 27B
2314 Valmont-sur-Lac

Rue des Tanneries 9
1623 Bourg-Neuf

Should not have
• mon projet ne doit pas contenir d'image en liens avec le massage ni la préparation mentale.

```html
<!DOCTYPE html>
<html lang="fr">
<head>
<meta charset="utf-8">
<title>Carte de visite – Loïc Vermande</title>
<link href="https://fonts.googleapis.com/css2?family=Inter:wght@400;500;700;800&display=swap" rel="stylesheet">
<style>
  :root {
    --page-bg: #e2e2e2;
    --card-bg: #ffffff;
    --ink: #111111;
    --card-edge: #9a9a9a;
  }
  * { box-sizing: border-box; margin: 0; padding: 0; }
  html, body { width: 1200px; height: 547px; overflow: hidden; }
  body {
    background: var(--page-bg);
    font-family: "Inter", Arial, sans-serif;
    color: var(--ink);
    position: relative;
  }
  .card {
    position: absolute;
    top: 120px;
    width: 540px;
    height: 308px;
    background: var(--card-bg);
    border: 1px solid var(--card-edge);
    box-shadow: 4px 6px 8px rgba(0,0,0,0.18);
    overflow: hidden;
  }
  .card--front { left: 40px; }
  .card--back { left: 620px; }

  .brand {
    position: absolute;
    left: 33px;
    top: 34px;
    display: flex;
    align-items: center;
    gap: 10px;
  }
  .brand__square { width: 22px; height: 22px; background: var(--ink); }
  .brand__text { display: flex; flex-direction: column; line-height: 1.1; }
  .brand__name { font-weight: 800; font-size: 19px; letter-spacing: 0.5px; }
  .brand__role { font-weight: 800; font-size: 7.5px; letter-spacing: 0.4px; text-transform: uppercase; }

  .holder-name {
    position: absolute;
    left: 41px;
    top: 118px;
    font-weight: 700;
    font-size: 29px;
  }
  .contact-list {
    position: absolute;
    left: 45px;
    top: 170px;
    list-style: none;
  }
  .contact-list li {
    display: flex;
    align-items: center;
    gap: 11px;
    font-size: 19px;
    height: 31.5px;
  }
  .contact-list svg { width: 15px; height: 15px; flex: none; }

  .side-mark {
    position: absolute;
    right: 6px;
    top: 0;
    height: 308px;
    width: 80px;
    display: flex;
    align-items: center;
    justify-content: center;
    writing-mode: vertical-rl;
    font-weight: 800;
    font-size: 36px;
    letter-spacing: 1px;
    white-space: nowrap;
  }

  .locations-title {
    position: absolute;
    left: 36px;
    top: 42px;
    font-weight: 700;
    font-size: 20px;
    letter-spacing: 0.2px;
  }
  .location {
    position: absolute;
    left: 34px;
    display: flex;
    align-items: center;
    gap: 22px;
    font-size: 19.5px;
    line-height: 26px;
  }
  .location--first { top: 100px; }
  .location--second { top: 190px; }
  .location svg { width: 24px; height: 32px; flex: none; }
</style>
</head>
<body>

<section class="card card--front" aria-label="Recto">
  <div class="brand">
    <span class="brand__square"></span>
    <div class="brand__text">
      <span class="brand__name">Loïc Vermande</span>
      <span class="brand__role">Massothérapeute / Préparateur Mental</span>
    </div>
  </div>

  <h1 class="holder-name">Loïc Vermande</h1>

  <ul class="contact-list">
    <li>
      <svg viewBox="0 0 24 24" aria-hidden="true"><path fill="currentColor" d="M2 9c0-3 4.5-5 10-5s10 2 10 5v2h-5V8.5c-1.5-.6-3.2-.9-5-.9s-3.5.3-5 .9V11H2zM6 12l2-3h8l2 3v8H6zm6 1.5a2.5 2.5 0 100 5 2.5 2.5 0 000-5z"/></svg>
      078 315 26 49
    </li>
    <li>
      <svg viewBox="0 0 24 24" aria-hidden="true"><path fill="currentColor" d="M2 5h20v14H2zm2 2v.5l8 5.5 8-5.5V7z"/></svg>
      info@loicvermande-exemple.ch
    </li>
    <li>
      <svg viewBox="0 0 24 24" aria-hidden="true"><g fill="none" stroke="currentColor" stroke-width="2"><circle cx="12" cy="12" r="9"/><ellipse cx="12" cy="12" rx="4" ry="9"/><path d="M3 12h18M5 7h14M5 17h14"/></g></svg>
      www.loicvermande-exemple.ch
    </li>
  </ul>

  <div class="side-mark" aria-hidden="true">Loïc Vermande</div>
</section>

<section class="card card--back" aria-label="Verso">
  <h2 class="locations-title">NOS EMPLACEMENTS</h2>

  <div class="location location--first">
    <svg viewBox="0 0 24 32" aria-hidden="true"><path fill="currentColor" fill-rule="evenodd" d="M12 0C5.4 0 0 5.2 0 11.6 0 20 12 32 12 32s12-12 12-20.4C24 5.2 18.6 0 12 0zm0 7a4.6 4.6 0 110 9.2A4.6 4.6 0 0112 7z"/></svg>
    <p>Chemin des Ormelets 27B<br>2314 Valmont-sur-Lac</p>
  </div>

  <div class="location location--second">
    <svg viewBox="0 0 24 32" aria-hidden="true"><path fill="currentColor" fill-rule="evenodd" d="M12 0C5.4 0 0 5.2 0 11.6 0 20 12 32 12 32s12-12 12-20.4C24 5.2 18.6 0 12 0zm0 7a4.6 4.6 0 110 9.2A4.6 4.6 0 0112 7z"/></svg>
    <p>Rue des Tanneries 9<br>1623 Bourg-Neuf</p>
  </div>

  <div class="side-mark" aria-hidden="true">Loïc Vermande</div>
</section>

</body>
</html>
```